Mobile Fitness snd Therapy Business Card Design

I need a business card designed for my mobile fitness and therapy business.

Please view the images that I have uploaded. I like the simplicity of the design that I have attached. I adapted it with my information

Target Market(s)

Those seeking personal training, injury rehabilitation or massage therapy.

Industry/Entity Type

Business

Contact Information for Business Card

Dylan Marwick - MSc, CAT(C), RMT, CSCS, Pn2
e-mail: dylan@vantrelo.com
website: www.vantrelo.com
instagram: @dylan_marwick

Font styles to use
Sans Serif

Colors
3176b5
0355a3

Requirements
Must have
• "Contact us to receive a FREE assessment"
• Services offered:
• Personal Training
• Golf Fitness
• Injury Rehab
• Massage Therapy
• Yoga
Nice to have
• Consistent colours with brand
• - Dark Blue: #232837
• - Blue: #5096f0
• Consistent look/feel with the website: www.vantrelo.com

```html
<!DOCTYPE html>
<html lang="en">
<head>
<meta charset="utf-8">
<title>Vantrelo Business Card</title>
<link rel="stylesheet" href="https://fonts.googleapis.com/css2?family=Open+Sans:wght@400;600;700&display=swap">
<style>
  :root {
    --stage: #a6a6a6;
    --card-dark: #000000;
    --card-light: #ffffff;
    --ink: #1b1b1b;
    --ink-light: #ffffff;
    --brand-blue: #3d72e8;
    --brand-navy: #232837;
    --icon-blue: #4a7fe6;
    --shadow: rgba(0, 0, 0, 0.45);
  }
  * { box-sizing: border-box; margin: 0; padding: 0; }
  html, body {
    width: 1200px; height: 900px; overflow: hidden;
    background: var(--stage);
    font-family: "Open Sans", Arial, sans-serif;
  }
  .card {
    position: absolute; top: 306px;
    width: 440px; height: 271px;
    box-shadow: 3px 4px 6px var(--shadow);
  }
  .card-front { left: 149px; background: var(--card-dark); color: var(--ink-light); }
  .card-back { left: 608px; background: var(--card-light); color: var(--ink); text-align: center; }

  .holder { position: absolute; left: 29px; top: 25px; }
  .holder-name {
    font-size: 15.5px; font-weight: 600; color: var(--brand-blue);
    text-transform: uppercase; letter-spacing: 0.1px; line-height: 1.2;
  }
  .holder-credentials { font-size: 10.5px; margin-top: 1px; }
  .contact-list { list-style: none; margin-top: 16px; }
  .contact-item {
    display: flex; align-items: center; gap: 5px;
    font-size: 12.5px; line-height: 16.5px;
  }
  .contact-icon { width: 11px; height: 11px; flex: none; }

  .front-brand {
    position: absolute; right: 30px; bottom: 30px; text-align: center;
  }
  .brand-name {
    font-size: 36px; font-weight: 700; letter-spacing: 3px; line-height: 1;
    text-transform: uppercase;
  }
  .front-brand .brand-name { color: var(--ink-light); }
  .brand-tagline {
    font-size: 11px; font-weight: 600; letter-spacing: 2.6px; margin-top: 6px;
  }

  .offer { font-size: 19px; font-weight: 600; margin-top: 26px; }
  .back-brand { margin-top: 14px; }
  .back-brand .brand-name { color: var(--brand-navy); font-size: 31px; }
  .back-brand .brand-tagline { color: var(--brand-navy); font-size: 9.5px; letter-spacing: 2.2px; margin-top: 4px; }
  .services-title {
    font-size: 22px; font-weight: 600; text-decoration: underline;
    text-underline-offset: 3px; text-decoration-thickness: 2px; margin-top: 24px;
  }
  .services-line { font-size: 20px; font-weight: 600; margin-top: 8px; line-height: 1.4; }
  .services-line + .services-line { margin-top: 10px; }
</style>
</head>
<body>
  <section class="card card-front">
    <div class="holder">
      <h1 class="holder-name">Dylan Marwick</h1>
      <p class="holder-credentials">MSc, CAT(C), RMT, CSCS, Pn2</p>
      <ul class="contact-list">
        <li class="contact-item">
          <svg class="contact-icon" viewBox="0 0 11 11" aria-hidden="true">
            <rect width="11" height="11" rx="2" fill="var(--icon-blue)"/>
            <rect x="2.2" y="3.2" width="6.6" height="4.6" fill="none" stroke="#fff" stroke-width="0.9"/>
            <path d="M2.2 3.2 L5.5 5.9 L8.8 3.2" fill="none" stroke="#fff" stroke-width="0.9"/>
          </svg>
          dylan@vantrelo.com
        </li>
        <li class="contact-item">
          <svg class="contact-icon" viewBox="0 0 11 11" aria-hidden="true">
            <rect width="11" height="11" rx="2" fill="var(--icon-blue)"/>
            <circle cx="5.5" cy="5.5" r="3.3" fill="none" stroke="#fff" stroke-width="0.9"/>
            <path d="M2.2 5.5 H8.8 M5.5 2.2 C4 4 4 7 5.5 8.8 C7 7 7 4 5.5 2.2" fill="none" stroke="#fff" stroke-width="0.7"/>
          </svg>
          www.vantrelo.com
        </li>
        <li class="contact-item">
          <svg class="contact-icon" viewBox="0 0 11 11" aria-hidden="true">
            <rect width="11" height="11" rx="2" fill="var(--icon-blue)"/>
          </svg>
          i@dylan_marwick
        </li>
      </ul>
    </div>
    <div class="front-brand">
      <p class="brand-name">Vantrelo</p>
      <p class="brand-tagline">NUTRITION - FITNESS - HEALTH</p>
    </div>
  </section>

  <section class="card card-back">
    <p class="offer">Contact us to receive a FREE assessment</p>
    <div class="back-brand">
      <p class="brand-name">Vantrelo</p>
      <p class="brand-tagline">NUTRITION - FITNESS - HEALTH</p>
    </div>
    <h2 class="services-title">SERVICES OFFERED</h2>
    <p class="services-line">Personal Training - Golf Fitness</p>
    <p class="services-line">Injury Rehab - Massage Therapy - Yoga</p>
  </section>
</body>
</html>
```